Flyer/Broschürre für Ambulanter Betreuungsdienst
Zielgruppe
Ambulanter Betreuungsdienst,Dienstleistungen für Senioren und Menschen mit Beeinträchtigung
Nach Paragraph 43b 45a/b & 53b SGBXI
Unterstützung im Alltag:
-Begleitung zu Arztbesuchen,Therapien &Terminbegleitung aller Art,
-Hilfe beim Einkaufen & Besorgungen + Transport
-Unterstützung bei der Tagesstrukturierung & Organisation im Alltag
-Erinnerungsservice zb. Einahme von Medikamenten ggbf. Kontrolle
-Begleitung zu Sportveranstaltungen,Theater uvm.
für zuverlässige Sicherheit und Orientierung.
-Gemeinsames Spazieren gehen ( Bewegungsangebote)
- Lesen & Vorlesen
-Gemeinsames Kochen und geselschaft leisten beim essen.
-Unterstützung bei Terminplanungen,Hilfe bei der komunikation mit Medizinischen Personal.
Soziale Betreuung & Aktivierung:
-Geselschaft leisten,Gespräche führen ;
-Freizeitaktivitäten Planen & Durchführen
-Gemeinsames Lesen und Vorlesen
-Karten & Brettspiele spielen
-Malen & Basteln
-Briefe schreiben,Emails verfassen
-Gemeinsam alte interessen wecken und neue finden.
-Angehörige entlasten
-kommunikation & Informationsaustausch über Fortschritte und Bedürfnisse
-Betreuung & Aktivierung für Menschen mit Demenz
-Erinnerungspflege,Biografie Arbeit
-Individuelle Betreuung
-Kurz und Langzeit Betreuung
-Nachtpflege
-Bewegungsangebote
-Spiele spielen zb. Brett & Gemeinschsftsspiele
Dienstleistungen Haushaltsbereich
-Reinigung von Böden(Saugen & Wischen)
-Reinigung Küche und Bad
-Bett frisch Beziehen
-Fenster Reinigung (innen & außen)
-Haustiere versorgen (mit dem Hund spazieren gehen)
-Wäsche waschen
-Dekorieren
-uvm
Aufgabenstellung
Freundliches Design , vertrauenswürdiges Erscheinungsbild mit warmen Farben.
Firmenname ( Sonnwerk) logo sollte einen Sonnwerk darstellen.
Slogan Text:
Verlässlichkeit und Fürsorge mit Herz & Verstand.
Format soll handlich und nicht zu klein sein,damit Senioren es gut lesen bzw erkennen können.

```html
<!DOCTYPE html>
<html lang="de">
<head>
<meta charset="utf-8">
<title>Sonnwerk – Ambulanter Betreuungsdienst</title>
<link rel="stylesheet" href="https://fonts.googleapis.com/css2?family=Nunito:wght@400;800;900&display=swap">
<style>
  :root {
    --berry: #7f1239;
    --peach: #f4a98f;
    --white: #ffffff;
    --photo-care: #d9cfc6;
    --photo-care-dark: #6f7f95;
    --photo-couple: #c58a5e;
    --photo-couple-dark: #5d8a9a;
    --illu-bg: #fbe6e6;
  }
  * { margin: 0; padding: 0; box-sizing: border-box; }
  html, body { width: 1200px; height: 848px; overflow: hidden; background: var(--berry); }
  body { font-family: "Nunito", Arial, sans-serif; color: var(--white); }
  .flyer { position: relative; width: 1200px; height: 848px; overflow: hidden; background: var(--berry); }
  .backdrop { position: absolute; inset: 0; }
  .brand {
    position: absolute; left: 905px; top: 50px;
    font-size: 50px; font-weight: 400; letter-spacing: 0.5px; color: var(--white);
  }
  .section-title {
    position: absolute; font-size: 18px; font-weight: 900; letter-spacing: 0.3px;
    padding-bottom: 6px; border-bottom: 1.5px solid var(--white);
  }
  .services-title { left: 40px; top: 314px; width: 323px; }
  .contact-title { left: 444px; top: 314px; width: 323px; }
  .areas-title { left: 445px; top: 659px; width: 323px; }
  .service-list { position: absolute; left: 40px; top: 371px; list-style: none; font-size: 19px; line-height: 24px; letter-spacing: 0.3px; }
  .service-list li { position: relative; padding-left: 34px; margin-bottom: 12px; }
  .service-list li::before {
    content: ""; position: absolute; left: 1px; top: 7px;
    width: 11px; height: 11px; border-radius: 50%; background: var(--white);
  }
  .contact-company { position: absolute; left: 444px; top: 372px; font-size: 19px; line-height: 24px; letter-spacing: 0.3px; }
  .contact-item { position: absolute; left: 444px; display: flex; align-items: center; font-size: 19px; line-height: 24px; letter-spacing: 0.4px; }
  .contact-item svg { width: 30px; height: 30px; margin-right: 30px; flex: none; }
  .contact-phone { top: 437px; }
  .contact-address { top: 486px; }
  .contact-mail { top: 550px; }
  .contact-web { top: 594px; }
  .areas-text { position: absolute; left: 445px; top: 708px; font-size: 19px; line-height: 24px; letter-spacing: 0.3px; }
  .slogan { position: absolute; left: 848px; top: 252px; font-size: 37px; font-weight: 900; line-height: 46.5px; letter-spacing: 0.2px; }
  .slogan-rule { position: absolute; left: 848px; top: 452px; width: 324px; border-top: 1.5px solid var(--white); }
  .tagline { position: absolute; left: 848px; top: 474px; font-size: 18.5px; line-height: 24px; letter-spacing: 0.3px; }
</style>
</head>
<body>
<main class="flyer">
  <svg class="backdrop" width="1200" height="848" viewBox="0 0 1200 848">
    <defs>
      <linearGradient id="care-tone" x1="0" y1="0" x2="1" y2="1">
        <stop offset="0" stop-color="var(--photo-care)"/>
        <stop offset="1" stop-color="var(--photo-care-dark)"/>
      </linearGradient>
      <linearGradient id="couple-tone" x1="0" y1="0" x2="1" y2="1">
        <stop offset="0" stop-color="var(--photo-couple-dark)"/>
        <stop offset="1" stop-color="var(--photo-couple)"/>
      </linearGradient>
    </defs>
    <rect class="photo-care" x="0" y="0" width="404" height="240" fill="url(#care-tone)" role="img" aria-label="Foto: Betreuerin schiebt einen Senior im Rollstuhl"/>
    <rect class="photo-couple" x="404" y="0" width="404" height="240" fill="url(#couple-tone)" role="img" aria-label="Foto: Seniorenpaar formt mit den Händen ein Herz"/>
    <path class="wave-peach" d="M0,107 C150,140 380,215 580,212 C800,208 1000,178 1200,172 L1200,848 L0,848 Z" fill="var(--peach)"/>
    <path class="wave-berry" d="M0,148 C180,192 380,250 560,250 C780,250 1000,190 1200,183 L1200,848 L0,848 Z" fill="var(--berry)"/>
    <ellipse class="illustration" cx="1000" cy="740" rx="182" ry="150" fill="var(--illu-bg)" role="img" aria-label="Illustration: Seniorenpaar Hand in Hand mit Pflanzen"/>
  </svg>

  <div class="brand">Sonnwerk</div>

  <h2 class="section-title services-title">Dienstleistungen im Haushalt</h2>
  <ul class="service-list">
    <li>Bodenreinigung<br>(Saugen &amp; Wischen)</li>
    <li>Reinigung Küche und Bad</li>
    <li>Bettenmachen (frisch Beziehen)</li>
    <li>Fensterreinigung (innen &amp; außen)</li>
    <li>Haustierversorgung<br>(z.B. Spazieren mit Hund)</li>
    <li>Wäsche waschen</li>
    <li>Dekorieren und vieles mehr</li>
  </ul>

  <h2 class="section-title contact-title">Kontakt</h2>
  <p class="contact-company">Sonnwerk<br>Ambulanter Betreuungsdienst</p>
  <p class="contact-item contact-phone">
    <svg viewBox="0 0 30 30" fill="none" stroke="#fff" stroke-width="1.5" stroke-linecap="round" stroke-linejoin="round"><path d="M7 4 L11 9 L9 12 C10 16 14 20 18 21 L21 19 L26 23 L23 27 C13 27 3 17 3 7 Z"/><path d="M17 6 A7 7 0 0 1 24 13"/><path d="M17 2 A11 11 0 0 1 28 13"/></svg>
    0345 918276
  </p>
  <p class="contact-item contact-address">
    <svg viewBox="0 0 30 30" fill="none" stroke="#fff" stroke-width="1.5"><path d="M15 25 C10 18 6 14 6 10 A9 9 0 0 1 24 10 C24 14 20 18 15 25 Z"/><circle cx="15" cy="10" r="3.5"/><ellipse cx="15" cy="27" rx="4" ry="1.3"/></svg>
    Lindenallee 7<br>04567 Sonnenthal
  </p>
  <p class="contact-item contact-mail">
    <svg viewBox="0 0 30 30" fill="none" stroke="#fff" stroke-width="1.5"><path d="M17 20 H3 V6 H25 V13"/><path d="M3 6 L14 14 L25 6"/><circle cx="23" cy="21" r="5"/><circle cx="23" cy="21" r="2"/></svg>
    info@sonnwerk-hilfe.de
  </p>
  <p class="contact-item contact-web">
    <svg viewBox="0 0 30 30" fill="none" stroke="#fff" stroke-width="1.5"><circle cx="15" cy="15" r="11"/><ellipse cx="15" cy="15" rx="5" ry="11"/><path d="M4 15 H26 M6 9 H24 M6 21 H24"/></svg>
    www.sonnwerk-hilfe.de
  </p>

  <h2 class="section-title areas-title">Versorgungsgebiete</h2>
  <p class="areas-text">Lindenfeld mit allen Stadtteilen<br>Birkenau, Eichwald, Talhof</p>

  <h1 class="slogan">Verlässlichkeit<br>und Fürsorge<br>mit Herz und<br>Verstand.</h1>
  <div class="slogan-rule"></div>
  <p class="tagline">Ambulanter Betreuungsdienst,<br>Dienstleistungen für Senioren und<br>Menschen mit Beeinträchtigung</p>
</main>
</body>
</html>
```